Vending Machine Graphics Required for The Copper Fern

Hi all,
I need vending machine graphics designed for a Pellix 386 (pictures uploaded) the surface is a back lit acyrlic on the front and 2 x stickers on the sides using our logo. There for 1 image for the front and 1 image for the sides.
Please keep the design simple and look snappy I have included samples for you to get a general idea.
The files will need to be supplied in pdf with bleed and crop marks, fonts should be outlined and images embedded
Budget has been doubled, please read brief and message if any questions. Thanks
For those designers that have accepted can we please see some preliminary designs ?
Thanks.

```html
<!DOCTYPE html>
<html lang="en">
<head>
<meta charset="utf-8">
<title>The Copper Fern – Vending Side Panel</title>
<link rel="stylesheet" href="https://fonts.googleapis.com/css2?family=Questrial&display=swap">
<style>
  :root {
    --sky: #cde8f8;
    --deep-water: #0b3f9e;
    --mid-water: #1e68cc;
    --bright-water: #3fa3ea;
    --sea-floor: #2f86a6;
    --label-rim: #1a4a94;
    --label-rim-light: #5fb6ea;
    --label-light: #ffffff;
    --label-tint: #bfe4f7;
    --brand-ink: #1a55a0;
    --mark-light: #3a8fd6;
    --sub-ink: #1c5d97;
  }
  html, body {
    margin: 0;
    padding: 0;
    width: 1200px;
    height: 2766px;
    overflow: hidden;
    background: var(--sky);
  }
  .panel {
    position: relative;
    width: 1200px;
    height: 2766px;
    background: var(--sky);
  }
  .bottle-art,
  .label {
    position: absolute;
    left: 0;
    top: 0;
    width: 1200px;
    height: 2766px;
  }
  .brand {
    position: absolute;
    left: 0;
    width: 1200px;
    text-align: center;
    font-family: "Questrial", sans-serif;
    white-space: nowrap;
  }
  .brand-mark {
    position: absolute;
    left: 445px;
    top: 880px;
    width: 310px;
    height: 310px;
    border-radius: 50%;
    background: var(--brand-ink);
  }
  .brand-name {
    top: 1262px;
    font-size: 126px;
    line-height: 1;
    color: var(--brand-ink);
    letter-spacing: -1px;
  }
  .brand-tagline {
    top: 1408px;
    font-size: 64px;
    line-height: 1;
    color: var(--sub-ink);
  }
</style>
</head>
<body>
<main class="panel">
  <svg class="bottle-art" viewBox="0 0 1200 2766" role="img" aria-label="Underwater photograph with sunlight rays and rising bubbles, shaped as a water bottle silhouette">
    <defs>
      <linearGradient id="waterDepth" x1="0" y1="0" x2="0" y2="1">
        <stop offset="0" stop-color="var(--bright-water)"/>
        <stop offset="0.3" stop-color="var(--mid-water)"/>
        <stop offset="0.72" stop-color="var(--deep-water)"/>
        <stop offset="1" stop-color="var(--sea-floor)"/>
      </linearGradient>
    </defs>
    <path d="M0 30 L735 26
             C748 110 752 210 752 300
             C760 470 820 600 880 700
             C925 780 938 880 938 980
             L938 2440
             C936 2560 930 2680 926 2766
             L0 2766 Z"
          fill="url(#waterDepth)"/>
  </svg>

  <svg class="label" viewBox="0 0 1200 2766" aria-hidden="true">
    <defs>
      <linearGradient id="labelFill" x1="0" y1="0" x2="0" y2="1">
        <stop offset="0" stop-color="var(--label-light)"/>
        <stop offset="0.5" stop-color="var(--label-tint)"/>
        <stop offset="1" stop-color="var(--label-light)"/>
      </linearGradient>
    </defs>
    <path d="M95 845 Q600 680 1105 845 L1200 1160 L1105 1480 Q600 1640 95 1480 L0 1160 Z"
          fill="none" stroke="var(--label-rim)" stroke-width="30" stroke-linejoin="round"/>
    <path d="M95 845 Q600 680 1105 845 L1200 1160 L1105 1480 Q600 1640 95 1480 L0 1160 Z"
          fill="url(#labelFill)" stroke="var(--label-rim-light)" stroke-width="10" stroke-linejoin="round"/>
  </svg>

  <div class="brand-mark"></div>
  <div class="brand brand-name">The Copper Fern</div>
  <div class="brand brand-tagline">Natural Spring Water</div>
</main>
</body>
</html>
```